Sunset Harbour Living Web Page

We need a web page design that has two intro pages - first being a 'home page', then a link to the second page that has the 'content tabs' and a 'call to action' (see below).

The business helps people that wish to retire to S.E.Asia (Thailand, Malaysia, Indonesia,The Philippines etc) - to enjoy the lifestyle and the remaining years of their lives. What attracts S.E.Asia to many people is the lower cost, the atmoshpere and beauty of the tropics and the vibrancy of the various countries.

People that are wishing to make the most of their retirement and are adventurous at a great bargain compared to the cost of their own countries will be interested.

We help them achieve this - visa, financials (tax, gov't payments etc), introduce them to the right people for property, clubs, retirement facilities, insurance and so forth.

Therefore we are providing an extremely wide ranging service and this site will provide broad but general information only - with a call to action to come and see us for more specific information and how we can help them specifically.

This site will be predominantly for travel and lifestyle, it will be linked with another financial services (financial planning) site later down the track.

The colour scheme is dark green and blue - as per the attached logo design. Photos and background just think lifestyle and S.E.Asia - beaches/mountains/water/recreational activities for retirees.

Target market is mostly those coming up to retirement to those that are already retired. But we also expect to have some interest with younger people that would like to find out more and plan for the future. So a broad age group but I would say mostly 40-70 yrs old.

On the first (Home) page we would like our company name 'Sunset Harbour Living', our logo (which will be on all pages) and a statement such as: “Imagine a retirement where your dreams are brought to life, and you have never felt more alive. Let us show you how”. Then a link to the second page.

We would like an uncluttered site. On the second (contents) page the tabs would be:

- Visa
- Property
- Financials
- Travel
- Insurance & Healthcare
- Medical Tourism
- Cost of living
- Weekly Blogs and articles
- Sunset Harbour Living story

We would also like a call to action on the second page - asking them to leave their contact details if they wish to learn more or sign up to our weekly newsletter/blog.

We are open to suggestions and your imaginations.

Thank you
Gerald

Font styles to use
Serif
Script

Colors
0255a3
3377b5
00a990
9bcb3c
abd036
33b8a4
85abd2
cadf82
86cfc6

Requirements
Must have
• I have been asked by the web designer to receive a 'Web Font' so that we can 'get off of Plixora'. Hope that makes sense.

```html
<!DOCTYPE html>
<html lang="en">
<head>
<meta charset="utf-8">
<title>Sunset Harbour Living — Home</title>
<link href="https://fonts.googleapis.com/css2?family=Alice&family=Lato:wght@900&family=Londrina+Solid:wght@300&family=Bubblegum+Sans&display=swap" rel="stylesheet">
<style>
  :root {
    --sky-top: #dbeef5;
    --sky-mid: #bfe3ea;
    --forest-light: #3f8f3a;
    --forest: #1f6b2a;
    --forest-deep: #0f4a22;
    --lake: #1a6a52;
    --name-ink: #0255a3;
    --lime: #abd036;
    --white: #ffffff;
    --ink: #1b1b10;
  }
  * { margin: 0; padding: 0; box-sizing: border-box; }
  html, body { width: 1200px; height: 923px; overflow: hidden; }
  body { font-family: "Lato", sans-serif; }
  .home {
    position: relative;
    width: 1200px;
    height: 923px;
    overflow: hidden;
  }
  .home__scenery {
    position: absolute;
    inset: 0;
    background:
      radial-gradient(ellipse 60% 20% at 80% 32%, rgba(120,170,170,0.55), transparent 70%),
      linear-gradient(180deg,
        var(--sky-top) 0%,
        var(--sky-mid) 24%,
        var(--forest-light) 33%,
        var(--forest) 50%,
        var(--lake) 62%,
        var(--forest-deep) 78%,
        var(--forest) 100%);
  }
  .brand {
    position: absolute;
    top: 176px;
    left: 0;
    width: 100%;
    display: flex;
    justify-content: center;
  }
  .brand__name {
    display: inline-flex;
    align-items: center;
    gap: 14px;
    font-family: "Alice", serif;
    font-size: 40px;
    line-height: 1;
    color: var(--name-ink);
  }
  .brand__dot {
    width: 22px;
    height: 22px;
    border-radius: 50%;
    background: var(--name-ink);
  }
  .pitch {
    position: absolute;
    top: 428px;
    left: 0;
    width: 100%;
    text-align: center;
    color: var(--white);
  }
  .pitch__imagine {
    font-family: "Alice", serif;
    font-size: 78px;
    line-height: 80px;
    margin-left: 156px;
  }
  .pitch__headline {
    margin-top: -6px;
    font-family: "Lato", sans-serif;
    font-weight: 900;
    font-size: 80px;
    line-height: 80px;
    letter-spacing: -1.5px;
    color: var(--lime);
  }
  .pitch__promise {
    margin-top: 2px;
    font-family: "Londrina Solid", sans-serif;
    font-weight: 300;
    font-size: 44px;
    line-height: 47px;
    letter-spacing: 0.5px;
    text-transform: uppercase;
    color: rgba(255,255,255,0.12);
    -webkit-text-stroke: 1.4px var(--white);
  }
  .cta-band {
    position: absolute;
    top: 756px;
    left: 0;
    width: 100%;
    height: 62px;
    background: var(--lime);
    display: flex;
    align-items: center;
    justify-content: center;
  }
  .cta-band__link {
    display: inline-flex;
    align-items: center;
    gap: 10px;
    font-family: "Bubblegum Sans", sans-serif;
    font-size: 26px;
    color: var(--ink);
    text-decoration: none;
    text-transform: uppercase;
  }
  .cta-band__icon { width: 24px; height: 24px; }
</style>
</head>
<body>
  <main class="home">
    <div class="home__scenery" role="img" aria-label="Tropical crater lake surrounded by lush green forested hills under a pale blue sky"></div>

    <header class="brand">
      <div class="brand__name"><span class="brand__dot"></span>Sunset Harbour Living</div>
    </header>

    <section class="pitch">
      <p class="pitch__imagine">Imagine</p>
      <h1 class="pitch__headline">A RETIREMENT</h1>
      <p class="pitch__promise">Where your dreams are brought to life,<br>and you have never felt more alive.</p>
    </section>

    <nav class="cta-band">
      <a class="cta-band__link" href="#contents">Let us show you how
        <svg class="cta-band__icon" viewBox="0 0 24 24" aria-hidden="true">
          <circle cx="12" cy="12" r="10.5" fill="none" stroke="#1b1b10" stroke-width="2"/>
          <path d="M10 7.5 L14.5 12 L10 16.5" fill="none" stroke="#1b1b10" stroke-width="2.2" stroke-linecap="round" stroke-linejoin="round"/>
        </svg>
      </a>
    </nav>
  </main>
</body>
</html>
```